Re-design of website

I have an existing website that I would like to improve. The functionality will remain the same but the overall look will need to be changed. I have some ideas of what i would like included and am also in need of someone else to input their own creative ideas. I am on a tight deadline to get these improvements made as I have many people being directed to the site via our advertising campaigns that are in full swing late next week. Thanks
Target Market(s)
The website provides a virtual space for families to learn more about our learning program which we operate out of Dubai and will soon spread to the other Emirates. The families are generally between 25-50 year old parents with children up to the age of 6. They are local Emirati's as well as expats.
Look and feel

```html
<!DOCTYPE html>
<html lang="en">
<head>
<meta charset="utf-8">
<title>Bright Sprouts – Home</title>
<link rel="stylesheet" href="https://fonts.googleapis.com/css2?family=Chewy&family=Open+Sans:wght@400;700&display=swap">
<style>
  :root {
    --sky: #9cd9fc;
    --mist: #eeeeee;
    --paper: #ffffff;
    --pink: #ee1c4e;
    --teal: #1aa6c4;
    --olive: #a3b617;
    --sun: #ffdf00;
    --ink: #222222;
    --body: #6b6b6b;
    --rule: #d8d8d8;
    --dot: #b9b9b9;
    --art-warm: #f3d9b0;
    --art-grey: #9a9a9a;
  }
  * { margin: 0; padding: 0; box-sizing: border-box; }
  html, body { width: 1200px; height: 713px; overflow: hidden; }
  body {
    position: relative;
    font-family: "Open Sans", Verdana, sans-serif;
    background: linear-gradient(to bottom, var(--sky) 0 314px, var(--mist) 314px 646px, var(--sky) 646px 713px);
  }
  .page { position: absolute; left: 161px; top: 30px; width: 878px; height: 637px; background: var(--paper); }
  .brand {
    position: absolute; left: 22px; top: 28px;
    font-family: "Open Sans", Verdana, sans-serif; font-weight: 700;
    font-size: 34px; color: var(--ink); line-height: 1;
  }
  .contact { position: absolute; left: 558px; top: 30px; font-size: 11.5px; color: var(--body); }
  .contact strong { color: var(--pink); font-weight: 700; font-size: 12.5px; margin-left: 3px; }
  .social { position: absolute; left: 621px; top: 49px; display: flex; gap: 6px; }
  .social span { width: 26px; height: 26px; border-radius: 50%; background: var(--dot); display: block; }
  .register {
    position: absolute; left: 738px; top: 30px; width: 119px; height: 41px;
    background: var(--sun); border-radius: 4px; text-align: center;
    font-size: 13px; line-height: 15px; color: #111; padding-top: 5px;
  }
  .register b { display: block; font-size: 12px; }
  .nav {
    position: absolute; left: 22px; top: 108px; width: 835px; height: 32px;
    background: var(--olive); border-radius: 4px; display: flex; overflow: hidden;
  }
  .nav a {
    color: #fff; text-decoration: none; font-weight: 700; font-size: 12px;
    display: flex; align-items: center; justify-content: center;
    border-left: 1px dashed rgba(255,255,255,.35);
  }
  .nav a:first-child { border-left: 0; }
  .nav a.current { background: var(--sun); color: #111; }
  h2 { font-family: "Chewy", "Comic Sans MS", cursive; font-weight: 400; font-size: 23px; color: var(--pink); position: absolute; line-height: 1; }
  h2 em { font-style: normal; color: var(--teal); }
  p, li { font-size: 11px; line-height: 12.5px; color: var(--body); }
  .intro { position: absolute; left: 22px; top: 196px; width: 490px; }
  .intro p + p { margin-top: 12px; }
  .philosophy { position: absolute; left: 22px; top: 361px; width: 490px; }
  .divider { position: absolute; left: 533px; top: 165px; height: 247px; border-left: 1px dashed var(--rule); }
  .program { position: absolute; left: 559px; top: 198px; width: 305px; list-style: none; }
  .program li { position: relative; padding-left: 14px; }
  .program li::before { content: "»"; position: absolute; left: 0; top: -1px; color: var(--olive); font-weight: 700; }
  .program li:nth-child(2) { margin-top: 15px; }
  .program li:nth-child(3) { margin-top: 15px; }
  .program li:nth-child(4) { margin-top: 14px; }
  .program li:nth-child(5) { margin-top: 15px; }
  .program li:nth-child(6) { margin-top: 14px; }
  .more { position: absolute; left: 559px; top: 392px; font-size: 11.5px; font-weight: 700; color: #111; text-decoration: none; }
  .talents {
    position: absolute; left: 21px; top: 436px; width: 829px; height: 172px;
    border-top: 1px dashed var(--rule); border-bottom: 1px dashed var(--rule); display: flex;
  }
  .talent { border-left: 1px dashed var(--rule); margin: 8px 0; position: relative; }
  .talent:first-child { border-left: 0; }
  .talent .art { position: absolute; left: 50%; top: 8px; transform: translateX(-50%); width: 74px; height: 108px; border-radius: 30px 30px 6px 6px; background: var(--art-warm); }
  .talent .art.mystery { background: var(--art-grey); }
  .talent h3 { position: absolute; left: 0; right: 0; top: 137px; text-align: center; font-size: 13px; font-weight: 700; color: var(--teal); }
  .talent h3.you { color: var(--pink); }
  .footer { position: absolute; left: 0; width: 1200px; top: 682px; text-align: center; font-size: 11.5px; color: #111; }
</style>
</head>
<body>
  <div class="page">
    <div class="brand">Bright Sprouts</div>
    <div class="contact">Call us: <strong>+971 555 012 345</strong></div>
    <div class="social" aria-label="Social links"><span></span><span></span><span></span></div>
    <a class="register">Register Your <b>Interest Here</b></a>

    <nav class="nav">
      <a class="current" style="width:90px">Home</a>
      <a style="width:132px">Oue Method</a>
      <a style="width:137px">The Program</a>
      <a style="width:90px">Media</a>
      <a style="width:114px">About Us</a>
      <a style="width:126px">Contact Us</a>
      <a style="width:146px">News &amp; Events</a>
    </nav>

    <h2 style="left:22px;top:162px">Welcome <em>!</em></h2>
    <div class="intro">
      <p>Research and leading academics agree that the early years of a child's life (defined as the 6 month old to 6 year old age group) is a critical time period to enhance the emotional and intellectual IQ of a child. 80% of your child's brain is developed by the age of 6 years old, to not offer heightened stimulation and specifically, right brain training during this period means that your child will not use a high proportion of their brain in their life time.</p>
      <p>Bright Sprouts Accelerated Learning Centre is the first a whole brain training program designed to maximise your child's potential during this key period of development.</p>
    </div>

    <h2 style="left:22px;top:321px">Our <em>Philosophy</em></h2>
    <div class="philosophy">
      <p>At Bright Sprouts, our philosophy and curriculum supports like-minded parents who want happiness for their children and want to see their children become the best they can be in their life. Our children are happy, confident and content with inquisitive minds and life skills that form the foundation of their lifetime of development and learning.</p>
    </div>

    <div class="divider"></div>

    <h2 style="left:559px;top:162px">Our <em>program :</em></h2>
    <ul class="program">
      <li>Enhance sensorial and critical thinking skills</li>
      <li>Develop photographic memory and recall skills</li>
      <li>Conditions children to love learning, develops an enquiring mind and encourages exploration</li>
      <li>Develops confidence and strengthens the bonds between children and their carers</li>
      <li>Develops children who delight in using all five senses</li>
      <li>Fosters creativity, intuition and confidence</li>
    </ul>
    <a class="more">READ MORE</a>

    <section class="talents">
      <div class="talent" style="width:146px"><div class="art" role="img" aria-label="Cartoon girl holding a paint palette and brush"></div><h3>Artist Ability</h3></div>
      <div class="talent" style="width:180px"><div class="art" role="img" aria-label="Cartoon boy sitting with a pinwheel"></div><h3>Sharp Imagination</h3></div>
      <div class="talent" style="width:179px"><div class="art mystery" role="img" aria-label="Grey silhouette of a child"></div><h3 class="you">Your Kid</h3></div>
      <div class="talent" style="width:180px"><div class="art" role="img" aria-label="Cartoon girl dancing in a green dress"></div><h3>Dance Ability</h3></div>
      <div class="talent" style="width:144px"><div class="art" role="img" aria-label="Cartoon boy playing with a football"></div><h3>Sports Talent</h3></div>
    </section>
  </div>

  <div class="footer">Copyright © 2013 <b>Bright Sprouts.</b> All Right Reserved.</div>
</body>
</html>
```